Doctor to Patient Management Website

I need a design for a health management website that connects doctors to patients. The website will consist of: A main page mainly describing our goal, services, and initiatives towards (Who we are AKA "About Us", Our services, Contact Us, Quick Links for health tips, Language selection, Find a doctor, search bar, Member Login Section, small glossary section below with links to all entities mentioned prior, Help section (Helpful tips and tutorials, Used to request help from admin, customer service, to resolve issues or get assistance). A profile page with two types:1) Doctor Profile: Doctor Personal info (First, Last, Middle Name, Title), Clinic, Hospital Info, Department, Credentials, Years of Experience, Patients rating, #Patients seen during the current week, #Patients seen in total, Picture, Link to email doctor, Link to print doctor's profile). Tabs for "About Me", "Contact Info", "Ratings & Comments", "Documents" (To be downloaded and uploaded by patient), "Patients (List of Patients alphabetical order by name)", "Calendar" (to see doctor's availability for booking) underneath all links. 2) Patient profile: About me, Personal Info, Height, Weight, Blood Type, Age, DOB, Name, etc..., Message and email link.Picture of patient with menu made of "Personal Data", "Biometrics", "Allergies", "Illnesses", "Medications", "Medical Procedures", "Doctors" treating the patient, "Documents" (To be downloaded and uploaded by patient). Underneath all, other patients he or she is related to (For example: family member, so patient can't connect to other patients who are family members)3) Login section: New Users will have option to register using:First Name (Required), Last Name, Middle (not required), Address (Not required), City (Required), Country (Required), Email (Not required), Phone Number (Required), Choose UserName, Password, Account Type (Doctor or Patient). Once registered, they will log in using UserName, Password, and Account_Type.Curent Users will log in using UserName, Password, and Account_Type and option to retrieve username or password.Pages to include (Login Page - Registration Page - Retrieve Username and Reset Password Page)Please see link below:https://lanternpost-media.example/importance-claiming-vitalrank-quopa-zeltra/Pictures are attached to this project as an inspirationFYI: Dummy text can be used to fill in the business, services, and descriptive information. Feel free to include your own ideas in the layout, design, categories, patterns, and more to and showcase your talent. Design and pictures provided are available as source of ideas.

Target Market(s)

Age: 21+ / Family Oriented / Medical Sector / Metropolitan Area / Educated and non Educated Users

Industry/Entity Type

Health Care

Number of Pages Required

5+ page

Font styles to use
Sans Serif

Colors

Designer to choose colors to be used in the design.

Requirements
Must have
• Thin layer design
• Simple font - No serif
• Clean menu with light but solid colors (No Gradient effect)
Nice to have
• Different color themes (2 or 3) can be combined
• Sample pictures for illustration (either as an ad or to go with the flow of your design)
• Dashboard Feel (Suggested but not required)
Should not have
• Artistic fonts - with Serif
• Dark color themes

```html
<!DOCTYPE html>
<html lang="en">
<head>
<meta charset="utf-8">
<title>Carewell — Health Management</title>
<link href="https://fonts.googleapis.com/css2?family=Roboto:ital,wght@0,300;0,400;0,500;0,700;0,900;1,400&family=Roboto+Condensed:wght@500;700&family=Open+Sans:wght@400;600&display=swap" rel="stylesheet">
<style>
:root{
  --blue:#1565c0;
  --blue-dark:#0d4fa3;
  --navy:#1c2a56;
  --navy-band:#1f2d5c;
  --teal:#1eaacc;
  --text:#555b66;
  --grey-bg:#eeeeee;
  --footer-bg:#f2f2f2;
  --white:#ffffff;
}
*{box-sizing:border-box;margin:0;padding:0}
html,body{width:1200px;height:3947px;overflow:hidden}
body{font-family:'Open Sans',sans-serif;color:var(--text);background:var(--white);position:relative}
.abs{position:absolute}
a{color:inherit;text-decoration:none}

/* top bar */
.topbar{position:absolute;left:0;top:0;width:1200px;height:37px;background:var(--blue);color:#fff;font-size:14px;font-family:'Roboto',sans-serif}
.topbar .item{position:absolute;top:9px;display:flex;align-items:center;gap:8px}
.search{position:absolute;left:600px;top:8px;width:240px;height:21px;background:#fff;border-radius:11px;font-size:10px;color:#888;padding:4px 12px}
.search svg{position:absolute;right:9px;top:5px}
.lang{position:absolute;left:1004px;top:10px;width:28px;height:17px;background:#e8ecf4;border-radius:2px}

/* header */
.header{position:absolute;left:0;top:37px;width:1200px;height:95px;background:#fff;box-shadow:0 2px 6px rgba(0,0,0,.08);z-index:3}
.brand{position:absolute;left:144px;top:24px;display:flex;align-items:center;gap:12px;font-family:'Roboto',sans-serif;font-weight:700;font-size:38px;color:var(--navy)}
.brand .mark{width:40px;height:40px;border:4px solid var(--navy);border-radius:50%}
.nav{position:absolute;left:418px;top:43px;display:flex;gap:30px;font-family:'Roboto',sans-serif;font-weight:500;font-size:16px;color:var(--navy);letter-spacing:.3px}

/* hero */
.hero{position:absolute;left:0;top:132px;width:1200px;height:740px;overflow:hidden}
.hero-photo{position:absolute;inset:0;background:linear-gradient(100deg,#e9eef3 0%,#dfe6ec 35%,#f2f5f7 60%,#cdd8e2 100%)}
.hero h1{position:absolute;left:184px;top:135px;font-family:'Roboto Condensed',sans-serif;font-weight:700;font-size:64px;color:var(--navy);letter-spacing:-.5px}
.hero p{position:absolute;left:188px;top:226px;width:420px;font-size:15px;line-height:24px;color:#333}
.btn-solid{display:inline-block;background:var(--blue);color:#fff;font-family:'Roboto',sans-serif;font-weight:700;border-radius:26px;text-align:center}
.hero .btn-solid{position:absolute;left:188px;top:336px;width:224px;height:48px;line-height:48px;font-size:20px}
.arrow{position:absolute;top:253px;width:34px;height:34px;border-radius:50%;background:#444c55;display:flex;align-items:center;justify-content:center}
.hero-wave{position:absolute;left:0;bottom:0;width:1200px;height:200px}

/* services */
.section-title{font-family:'Roboto',sans-serif;font-size:38px;color:var(--navy);text-align:center}
.section-title b{font-weight:900}
.services-title{position:absolute;left:0;top:832px;width:1200px}
.service{position:absolute;top:943px;width:200px;text-align:center}
.service .icon{width:110px;height:110px;border-radius:50%;background:var(--teal);margin:0 auto;display:flex;align-items:center;justify-content:center}
.service h3{margin-top:29px;font-family:'Roboto',sans-serif;font-weight:700;font-size:15px;color:var(--blue)}
.service p{margin-top:16px;font-size:13px;line-height:22px;color:#555}

/* about */
.about{position:absolute;left:0;top:1321px;width:624px;height:503px;background:var(--grey-bg)}
.split-photo{position:absolute}
.block-title{font-family:'Roboto',sans-serif;font-size:46px;color:var(--navy)}
.block-title b{font-weight:900}
.block-title span{font-weight:300}
.body-copy{font-size:15px;line-height:26px;color:#555}
.btn-outline{display:inline-block;border:2px solid var(--blue);color:var(--blue);border-radius:22px;font-family:'Roboto',sans-serif;font-weight:500;font-size:17px;text-align:center}

/* tips */
.tips{position:absolute;left:624px;top:1824px;width:576px;height:500px;background:var(--grey-bg)}
.tips ul{list-style:none}
.tips li{display:flex;align-items:center;gap:12px;font-size:15px;color:#555;height:31px}

/* help */
.help-title{position:absolute;left:145px;top:2451px;font-family:'Roboto',sans-serif;font-weight:500;font-size:30px;color:var(--navy);letter-spacing:1px}
.help-sub{position:absolute;left:145px;top:2500px;width:400px;font-family:'Roboto',sans-serif;font-weight:500;font-size:21px;line-height:30px;color:#26357a}
.quote{position:absolute;left:145px;top:2582px;width:380px;font-family:'Roboto',sans-serif;font-size:17px;line-height:29px;color:#444}
.quote .qm{color:#9fc2e6;font-size:26px;font-weight:700}
.author{position:absolute;left:143px;top:2747px;display:flex;align-items:center;gap:20px;font-family:'Roboto',sans-serif}
.avatar{width:52px;height:52px;border-radius:50%;background:linear-gradient(#c9b59a,#8a7a66)}
.author b{display:block;font-size:11px;color:var(--navy);font-weight:700}
.author i{font-size:11px;color:#555}
.dots{position:absolute;left:148px;top:2838px;display:flex;gap:11px}
.dots span{width:8px;height:8px;border-radius:50%;background:#c9d3de}
.dots span.on{background:var(--teal)}
.video{position:absolute;left:587px;top:2463px;width:468px;height:348px;border-radius:4px;background:linear-gradient(120deg,#5c6b78,#a9b3ba 50%,#6c7780);box-shadow:0 3px 10px rgba(0,0,0,.2)}
.play{position:absolute;left:206px;top:146px;width:58px;height:58px;border-radius:50%;background:#151515;display:flex;align-items:center;justify-content:center}

/* glossary */
.glossary{position:absolute;left:0;top:2969px;width:1200px;height:530px;background:var(--navy-band);overflow:hidden}
.glossary h2{position:absolute;left:0;top:90px;width:1200px;text-align:center;font-family:'Roboto',sans-serif;font-weight:900;font-size:46px;color:#fff;letter-spacing:1px}
.glossary p{position:absolute;left:160px;top:162px;width:880px;text-align:center;font-family:'Roboto',sans-serif;font-size:16px;line-height:33px;color:#e6ebf5}
.glossary .btn-solid{position:absolute;left:518px;top:293px;width:163px;height:46px;line-height:46px;font-size:19px;font-weight:500}
.gl-wave{position:absolute;left:0;bottom:0;width:1200px;height:220px}

/* footer */
.footer{position:absolute;left:0;top:3499px;width:1200px;height:323px;background:var(--footer-bg)}
.col-title{font-family:'Roboto',sans-serif;font-weight:500;font-size:23px;color:var(--navy)}
.fcol{position:absolute;top:50px}
.small{font-family:'Roboto',sans-serif;font-size:12px;line-height:19px;color:#444}
.email-field{width:270px;height:38px;border:1px solid #ddd;border-radius:20px;background:#fff;font-size:10px;color:#777;padding:12px 16px;margin-top:18px}
.subscribe{margin-top:14px;width:138px;height:32px;line-height:32px;font-size:14px}
.contact-row{display:flex;gap:16px;margin-top:16px}
.cicon{width:26px;height:26px;background:var(--blue);border-radius:3px;flex:none;display:flex;align-items:center;justify-content:center}
.links{list-style:none;margin-top:18px}
.links li{font-family:'Roboto',sans-serif;font-size:13px;line-height:26px;color:#444}
.social{display:flex;gap:6px;margin-top:20px}
.social span{width:30px;height:30px;border-radius:50%;border:1.5px solid #555}
.copyright{position:absolute;left:0;top:3822px;width:1200px;height:125px;background:var(--footer-bg);border-top:1px solid #ddd;text-align:center;padding-top:56px;font-family:'Roboto',sans-serif;font-size:14px;color:#333}
</style>
</head>
<body>

<div class="topbar">
  <div class="item" style="left:144px">
    <svg width="14" height="14" viewBox="0 0 24 24"><path fill="#fff" d="M6.6 10.8a15 15 0 0 0 6.6 6.6l2.2-2.2c.3-.3.7-.4 1-.2 1.1.4 2.3.6 3.6.6.6 0 1 .4 1 1V20c0 .6-.4 1-1 1A17 17 0 0 1 3 4c0-.6.4-1 1-1h3.5c.6 0 1 .4 1 1 0 1.3.2 2.5.6 3.6.1.3 0 .7-.2 1z"/></svg>
    555-0142-7788
  </div>
  <div class="item" style="left:303px">
    <svg width="15" height="12" viewBox="0 0 24 18"><rect x="1" y="1" width="22" height="16" rx="2" fill="#fff"/><path d="M2 2l10 8 10-8" stroke="#1565c0" stroke-width="2" fill="none"/></svg>
    hello@carewell-health.example
  </div>
  <div class="search">Search here
    <svg width="11" height="11" viewBox="0 0 24 24"><circle cx="10" cy="10" r="7" stroke="#333" stroke-width="3" fill="none"/><path d="M15 15l6 6" stroke="#333" stroke-width="3"/></svg>
  </div>
  <div class="item" style="left:855px;font-weight:500">
    <svg width="11" height="13" viewBox="0 0 20 24"><rect x="2" y="10" width="16" height="13" rx="2" fill="#fff"/><path d="M5 10V7a5 5 0 0 1 10 0v3" stroke="#fff" stroke-width="3" fill="none"/></svg>
    MEMBER LOGIN
  </div>
  <div class="lang" aria-label="Language selection"></div>
  <svg class="abs" style="left:1044px;top:16px" width="9" height="6" viewBox="0 0 10 6"><path d="M0 0h10L5 6z" fill="#fff"/></svg>
</div>

<header class="header">
  <div class="brand"><span class="mark"></span>Carewell</div>
  <nav class="nav">
    <a>HOME</a><a>ABOUT US</a><a>OUR SERVICES</a><a>BLOG</a><a>FIND A DOCTOR</a><a>CONTACT US</a>
  </nav>
</header>

<section class="hero">
  <div class="hero-photo" role="img" aria-label="Smiling doctor in a white coat with a stethoscope, arms crossed, beside a laptop in a bright clinic"></div>
  <h1>Health Management</h1>
  <p>Sed ut perspiciatis unde omnis iste natus error sit voluptatem accusantium doloremque laudantium, totam rem aperiam, eaque ipsa quae ab illo inventore veritatis</p>
  <a class="btn-solid">FIND A DOCTOR</a>
  <div class="arrow" style="left:58px"><svg width="12" height="12" viewBox="0 0 12 12"><path d="M8 1L3 6l5 5" stroke="#fff" stroke-width="2" fill="none"/></svg></div>
  <div class="arrow" style="left:1106px"><svg width="12" height="12" viewBox="0 0 12 12"><path d="M4 1l5 5-5 5" stroke="#fff" stroke-width="2" fill="none"/></svg></div>
  <svg class="hero-wave" viewBox="0 0 1200 200" preserveAspectRatio="none">
    <path d="M0 70 C 250 200, 600 150, 900 80 C 1030 50, 1130 60, 1200 110 L1200 200 L0 200Z" fill="#fff"/>
    <path d="M300 150 C 600 170, 850 70, 1050 60 C 1130 58, 1180 80, 1200 110 L1200 200 C 1150 120, 1050 110, 950 130 C 750 175, 500 175, 300 150Z" fill="#1565c0"/>
    <path d="M330 160 C 600 180, 850 95, 1040 85 C 1120 82, 1170 100, 1200 130" stroke="#fff" stroke-width="5" fill="none"/>
    <path d="M0 70 C 250 200, 600 160, 900 90" stroke="#1565c0" stroke-width="3" fill="none"/>
  </svg>
</section>

<h2 class="section-title services-title"><b>OUR</b> SERVICES</h2>

<div class="service" style="left:134px">
  <div class="icon"><svg width="54" height="54" viewBox="0 0 54 54" fill="none" stroke="#fff" stroke-width="2.5"><circle cx="27" cy="17" r="9"/><path d="M10 50c0-11 7-17 17-17s17 6 17 17"/><path d="M22 34l5 8 5-8"/></svg></div>
  <h3>QUIS AUTEM VEL EUM</h3>
  <p>Sed ut perspiciatis unde omnis iste natus error sit voluptatem santium doloremque udantium, totam rem aperiam</p>
</div>
<div class="service" style="left:376px">
  <div class="icon"><svg width="54" height="54" viewBox="0 0 54 54" fill="none" stroke="#fff" stroke-width="2.5"><path d="M27 40s-12-7-12-16a6 6 0 0 1 12-2 6 6 0 0 1 12 2c0 9-12 16-12 16z"/><path d="M6 30l8 8h10M48 24l-8-8H30"/></svg></div>
  <h3>QUIS AUTEM VEL EUM</h3>
  <p>Sed ut perspiciatis unde omnis iste natus error sit voluptatem santium doloremque udantium, totam rem aperiam</p>
</div>
<div class="service" style="left:618px">
  <div class="icon"><svg width="54" height="54" viewBox="0 0 54 54" fill="none" stroke="#fff" stroke-width="2.5"><rect x="12" y="8" width="26" height="36" rx="2"/><path d="M18 18h14M18 25h14M18 32h8"/><path d="M34 36l10 10"/><circle cx="32" cy="34" r="5"/></svg></div>
  <h3>QUIS AUTEM VEL EUM</h3>
  <p>Sed ut perspiciatis unde omnis iste natus error sit voluptatem santium doloremque udantium, totam rem aperiam</p>
</div>
<div class="service" style="left:863px">
  <div class="icon"><svg width="54" height="54" viewBox="0 0 54 54" fill="none" stroke="#fff" stroke-width="2.5"><path d="M27 48V22"/><circle cx="27" cy="16" r="5"/><path d="M27 30l-10-8M27 36l10-8M10 14l4 4M44 14l-4 4M27 4v4"/></svg></div>
  <h3>QUIS AUTEM VEL EUM</h3>
  <p>Sed ut perspiciatis unde omnis iste natus error sit voluptatem santium doloremque udantium, totam rem aperiam</p>
</div>

<section class="about">
  <h2 class="block-title abs" style="left:145px;top:78px"><b>ABOUT</b> <span>CAREWELL</span></h2>
  <p class="body-copy abs" style="left:145px;top:157px;width:440px">Sed ut perspiciatis unde omnis iste natus error sit voluptatem accusantium doloremque laudantium, totam rem aperiam, eaque ipsa quae ab illo inventore veritatis et quasi architecto beatae vitae dicta sunt explicabo. Nemo enim ipsam voluptatem quia voluptas sit aspernatur aut odit aut fugit, sed quia conse-quuntur magni dolores eos qui ratione</p>
  <a class="btn-outline abs" style="left:145px;top:372px;width:172px;height:42px;line-height:38px">READ MORE</a>
</section>
<div class="split-photo" style="left:624px;top:1321px;width:576px;height:503px;background:linear-gradient(120deg,#b9c7d6,#e4eaf0 55%,#c7ccd1)" role="img" aria-label="Smiling female doctor with a stethoscope in front of colleagues in a clinic"></div>

<div class="split-photo" style="left:0;top:1824px;width:624px;height:500px;background:linear-gradient(135deg,#0b3f7a,#1f6fb8 45%,#5fb3e6 70%,#124f8f)" role="img" aria-label="Doctor holding a tablet showing a glowing holographic human body with DNA strands and pills"></div>
<section class="tips">
  <h2 class="block-title abs" style="left:76px;top:70px"><b>HEALTH</b> <span>TIPS</span></h2>
  <p class="body-copy abs" style="left:79px;top:150px;width:430px;font-size:14px;line-height:24px">Sed ut perspiciatis unde omnis iste natus error sit voluptatem accusantium doloremque laudantium, totam</p>
  <ul class="abs" style="left:79px;top:221px">
    <li><svg width="14" height="14" viewBox="0 0 14 14"><circle cx="7" cy="7" r="6" stroke="#333" stroke-width="1.4" fill="none"/><path d="M6 4l3 3-3 3" stroke="#333" stroke-width="1.4" fill="none"/></svg>Nulla scelerisque felis nec tincidunt varius.</li>
    <li><svg width="14" height="14" viewBox="0 0 14 14"><circle cx="7" cy="7" r="6" stroke="#333" stroke-width="1.4" fill="none"/><path d="M6 4l3 3-3 3" stroke="#333" stroke-width="1.4" fill="none"/></svg>Ut mollis erat at vehicula efficitur.</li>
    <li><svg width="14" height="14" viewBox="0 0 14 14"><circle cx="7" cy="7" r="6" stroke="#333" stroke-width="1.4" fill="none"/><path d="M6 4l3 3-3 3" stroke="#333" stroke-width="1.4" fill="none"/></svg>Sed in ligula id purus molestie consequat.</li>
    <li><svg width="14" height="14" viewBox="0 0 14 14"><circle cx="7" cy="7" r="6" stroke="#333" stroke-width="1.4" fill="none"/><path d="M6 4l3 3-3 3" stroke="#333" stroke-width="1.4" fill="none"/></svg>Cras ut tortor vehicula, posuere tellus id, porta mauris.</li>
  </ul>
  <a class="btn-outline abs" style="left:79px;top:375px;width:172px;height:42px;line-height:38px">READ MORE</a>
</section>

<h2 class="help-title">HELP</h2>
<p class="help-sub">Nemo enim ipsam voluptatem quia tas voluptatem</p>
<p class="quote"><span class="qm">«</span> Sed ut perspiciatis unde omnis iste natus error sit voluptatem accusantium doloremque laudantium, totam rem aperiam, eaque ipsa quae ab illo inventore veritatis et quasi architecto beatae vitae dicta <span class="qm">»</span></p>
<div class="author">
  <div class="avatar" role="img" aria-label="Portrait of the customer care lead"></div>
  <div><b>NORA WHITCOMBE</b><i>Carewell</i></div>
</div>
<div class="dots"><span></span><span class="on"></span><span></span><span></span></div>
<div class="video" role="img" aria-label="Video still of a care team meeting around a table with a tablet">
  <div class="play"><svg width="20" height="22" viewBox="0 0 20 22"><path d="M3 1l16 10L3 21z" fill="#fff"/></svg></div>
</div>

<section class="glossary">
  <h2>GLOSSARY</h2>
  <p>Sed ut perspiciatis unde omnis iste natus error sit voluptatem accusantium doloremque laudantium, totam rem aperiam, eaque ipsa quae ab illo inventore veritatis et quasi architecto beatae vitae dicta sunt explicabo. Nemo enim ipsam voluptatem quia voluptas sit aspernatur aut odit aut fugit, sed quia consequuntur magni</p>
  <a class="btn-solid">Read More →</a>
  <svg class="gl-wave" viewBox="0 0 1200 220" preserveAspectRatio="none">
    <path d="M0 40 C 200 130, 500 200, 800 170 C 1000 150, 1120 130, 1200 150 L1200 220 L0 220Z" fill="#f2f2f2"/>
    <path d="M0 20 C 200 120, 500 190, 800 160 C 1000 140, 1120 120, 1200 140 L1200 160 C 1120 140, 1000 160, 800 180 C 500 210, 200 150, 0 60Z" fill="#1565c0"/>
    <path d="M0 40 C 200 135, 500 200, 800 172 C 1000 152, 1120 132, 1200 150" stroke="#fff" stroke-width="5" fill="none"/>
  </svg>
</section>

<footer class="footer">
  <div class="fcol" style="left:145px">
    <h3 class="col-title">Sign up for newsletter</h3>
    <p class="small" style="margin-top:18px;width:280px">Excepteur sint occaecat cupidatat non proident, sunt in culpa qui officia deserunt</p>
    <div class="email-field">Enter email</div>
    <a class="btn-solid subscribe">SUBSCRIBE</a>
  </div>
  <div class="fcol" style="left:484px">
    <h3 class="col-title">Contact Us</h3>
    <div class="contact-row"><span class="cicon"><svg width="12" height="14" viewBox="0 0 12 16"><path d="M6 0a6 6 0 0 1 6 6c0 4-6 10-6 10S0 10 0 6a6 6 0 0 1 6-6z" fill="#fff"/><circle cx="6" cy="6" r="2" fill="#1565c0"/></svg></span><p class="small">Carewell<br>208 Alder Lane, 2nd floor<br>Riverton, ST 40210</p></div>
    <div class="contact-row"><span class="cicon"><svg width="13" height="13" viewBox="0 0 24 24"><path fill="#fff" d="M6.6 10.8a15 15 0 0 0 6.6 6.6l2.2-2.2c.3-.3.7-.4 1-.2 1.1.4 2.3.6 3.6.6.6 0 1 .4 1 1V20c0 .6-.4 1-1 1A17 17 0 0 1 3 4c0-.6.4-1 1-1h3.5c.6 0 1 .4 1 1 0 1.3.2 2.5.6 3.6.1.3 0 .7-.2 1z"/></svg></span><p class="small">Phone:<br>1.555.014.2290</p></div>
    <div class="contact-row"><span class="cicon"><svg width="14" height="11" viewBox="0 0 24 18"><rect x="1" y="1" width="22" height="16" rx="2" fill="#fff"/><path d="M2 2l10 8 10-8" stroke="#1565c0" stroke-width="2" fill="none"/></svg></span><p class="small">Email :<br>hello@carewell-health.example</p></div>
  </div>
  <div class="fcol" style="left:755px">
    <h3 class="col-title">Quick Links</h3>
    <ul class="links"><li>Home</li><li>About Us</li><li>Our Services</li><li>Blog</li><li>Find A Doctor</li><li>Contact Us</li></ul>
  </div>
  <div class="fcol" style="left:926px">
    <h3 class="col-title">Follow us</h3>
    <div class="social" aria-label="Social links"><span></span><span></span><span></span><span></span></div>
  </div>
</footer>
<div class="copyright">© Copyright 2019 Carewell. All Rights Reserved.</div>

</body>
</html>
```